Change base color of existing graphics

We have an existing graphic(s) that is a border to our web page. Our client has requested a color change of the base color to 0,120,193. We do NOT have the original PSD files.

Top corners are rounded and contain corporate logos which will be sent to those with interest in the project.

This does not need to be a pixel perfect copy of the existing images, but it is the baseline they have requested so it should be similar in feel but there is some freedom in design.

The large square buttons in the screen shot are client provided and will not change.

What I would like returned are cut images identical to the attachments so they can simply be swapped out on the website. Would also like original PSD or other format that is used to generate.

Any questions, please do not hesitate to contact.

```html
<!DOCTYPE html>
<html lang="en">
<head>
<meta charset="utf-8">
<title>Page Border Frame</title>
<link rel="stylesheet" href="https://fonts.googleapis.com/css2?family=Open+Sans&display=swap">
<style>
  :root {
    --brand-base: #0078c1;
    --frame-edge: #0a5fa3;
    --panel: #ffffff;
    --shine: #f2f7fc;
    --shine-soft: #8fc0e2;
    --shadow: #9aa3ad;
  }
  html, body {
    margin: 0;
    padding: 0;
    width: 1200px;
    height: 1004px;
    overflow: hidden;
    background: var(--panel);
    font-family: "Open Sans", sans-serif;
  }
  .page-frame {
    position: relative;
    width: 1200px;
    height: 1004px;
  }
  .frame-border {
    position: absolute;
    left: 6px; top: 2px;
    width: 1189px; height: 997px;
    border: 2px solid var(--frame-edge);
    border-radius: 6px;
    box-sizing: border-box;
    background: var(--panel);
  }
  .header-bar {
    position: absolute;
    left: 8px; top: 4px;
    width: 1185px; height: 44px;
    background: var(--brand-base);
    border-radius: 4px 4px 0 0;
    box-shadow: 0 3px 3px var(--shadow);
  }
  .header-logo-slot {
    position: absolute;
    left: 0; top: 0;
    width: 196px; height: 44px;
    border-radius: 4px 0 0 0;
    background: linear-gradient(90deg, var(--brand-base) 0%, var(--shine-soft) 20%, var(--shine) 48%, #b3d4ec 80%, var(--brand-base) 100%);
  }
  .footer-bar {
    position: absolute;
    left: 8px; top: 952px;
    width: 1185px; height: 45px;
    background: var(--brand-base);
    border-radius: 0 0 4px 4px;
    box-shadow: 0 -2px 2px var(--shadow);
  }
</style>
</head>
<body>
  <div class="page-frame">
    <div class="frame-border"></div>
    <div class="header-bar">
      <div class="header-logo-slot" role="img" aria-label="Logo area with light highlight"></div>
    </div>
    <div class="footer-bar"></div>
  </div>
</body>
</html>
```